Open Window; Sunrise Table, River Walk Rack Card

We want an additional 2 page (front and page) 3.67" x 8.5" rack card. This rack card is now the 2nd of the series . The first one is already completed/finalized and attached (Sunrise Table River Walk Rack Card PDF).
Use the text on the word document for the included Open Window Rack card. Please use the Sunrise Table River Walk Rack card as the template to mimic. We would like all subsequent rack cards to have a similar look and feel.
The document is for older readers. Do not put text over graphics and keep it simple and easy to read with high contrast.
We want some very simple design element(s) incorporated that convey Native American communities or heritage. But NO headdress, teepee graphics, etc. At the top, of the first page we would like a collage of healthy food images. This can include fish, chicken, fresh vegetables, berries, brown rice, etc. Please remember to include the funding statement - it can be in a very small font 6/7 point. For more information about our project, please visit https://pelmorvo.org/kite-lane/

```html
<!DOCTYPE html>
<html lang="en">
<head>
<meta charset="utf-8">
<title>Open Window – Sunrise Table, River Walk Rack Card</title>
<link rel="stylesheet" href="https://fonts.googleapis.com/css2?family=Bowlby+One&family=Roboto:ital,wght@0,300;0,400;0,500;0,700;1,500&family=Montserrat:wght@700;800&display=swap">
<style>
  :root {
    --maroon: #6b1f1c;
    --teal: #4fb3c8;
    --teal-dark: #1f7a85;
    --salmon: #c0665a;
    --peach: #f3b27a;
    --ink: #3a2a28;
    --paper: #f5f5f3;
    --stage: #d9d9d9;
    --label: #6d6d6d;
    --tick: #7fa6c4;
    --fine: #777;
  }
  * { box-sizing: border-box; margin: 0; padding: 0; }
  html, body { width: 1200px; height: 4500px; overflow: hidden; }
  body { background: var(--stage); font-family: "Roboto", sans-serif; color: var(--ink); position: relative; }

  .side-label {
    position: absolute; left: 0; width: 1200px; text-align: center;
    font-family: "Montserrat", sans-serif; font-weight: 800; font-size: 62px;
    letter-spacing: 14px; color: var(--label);
  }
  .side-label.front-label { top: 170px; }
  .side-label.back-label { top: 2292px; }

  .card {
    position: absolute; left: 189px; width: 821px; height: 1902px;
    background: var(--paper); box-shadow: 0 8px 18px rgba(0,0,0,.28); overflow: hidden;
  }
  .card.front { top: 276px; }
  .card.back { top: 2407px; }
  .card > * { position: absolute; }

  .food-collage {
    left: 0; top: 0; width: 821px; height: 420px;
    background: linear-gradient(100deg, #6a3a2e 0%, #7c9a4a 30%, #e0784a 52%, #4e8a3a 72%, #c8322c 100%);
  }
  .title-line {
    left: 0; width: 821px; text-align: center; font-family: "Bowlby One", sans-serif;
    line-height: 1; letter-spacing: 1px;
  }
  .title-line.one { top: 395px; font-size: 76px; color: var(--maroon); }
  .title-line.two { top: 468px; font-size: 76px; color: var(--teal); }

  .section-title {
    left: 0; width: 821px; top: 556px; text-align: center;
    font-family: "Roboto", sans-serif; font-weight: 700; font-size: 40px; color: var(--maroon);
  }
  .intro {
    left: 60px; width: 701px; top: 608px; text-align: center;
    font-size: 27px; line-height: 34px; color: var(--salmon);
  }
  .zigzag-band {
    left: 0; width: 821px; height: 40px;
    background: linear-gradient(180deg, #b9b3ad, #8d8580);
  }
  .front .zigzag-band { top: 761px; }
  .back .zigzag-band { top: 1269px; }

  .bar {
    left: 0; width: 821px; background: var(--maroon); color: var(--peach);
    font-family: "Montserrat", sans-serif; font-weight: 700; text-align: center;
    display: flex; align-items: center; justify-content: center;
  }
  .bar.changes { top: 803px; height: 59px; font-size: 25px; }
  .bar.doctor { top: 1525px; height: 89px; font-size: 24px; line-height: 31px; }

  .checklist { list-style: none; }
  .checklist li { position: relative; padding-left: 36px; }
  .checklist li::before {
    content: ""; position: absolute; left: 0; top: 8px; width: 18px; height: 18px;
    border: 2px solid var(--tick);
  }
  .checklist li::after {
    content: ""; position: absolute; left: 6px; top: 6px; width: 7px; height: 13px;
    border-right: 3px solid var(--tick); border-bottom: 3px solid var(--tick); transform: rotate(40deg);
  }
  .front .checklist { left: 70px; top: 880px; width: 690px; font-size: 27px; line-height: 34px; }
  .front .checklist li { margin-bottom: 9px; }
  .checklist strong { color: var(--maroon); font-weight: 700; }

  .quote { left: 40px; width: 741px; top: 1625px; text-align: center; }
  .quote-text { font-size: 28px; line-height: 34px; font-weight: 700; color: var(--maroon); }
  .quote-mark { color: var(--teal); font-family: "Bowlby One", sans-serif; font-size: 60px; line-height: 0; vertical-align: -18px; }
  .quote-by { font-size: 22px; margin-top: 6px; }

  .rule { left: 30px; width: 761px; height: 2px; background: var(--teal); top: 1738px; }
  .tagline {
    left: 30px; width: 761px; top: 1750px; text-align: center;
    font-family: "Montserrat", sans-serif; font-weight: 700; font-size: 24px; line-height: 30px; color: var(--teal);
  }
  .funding { left: 30px; width: 761px; font-size: 13.5px; line-height: 17px; color: var(--fine); }
  .front .funding { top: 1807px; }
  .back .funding { top: 1817px; }
  .bottom-strip { left: 0; bottom: 0; width: 821px; height: 16px; background: var(--teal-dark); }

  /* back */
  .make-title {
    left: 0; width: 821px; top: 55px; text-align: center;
    font-family: "Bowlby One", sans-serif; font-size: 56px; color: var(--maroon);
  }
  .make-title span { color: var(--teal); }
  .recipe-name {
    left: 40px; width: 400px; top: 152px; text-align: center;
    font-family: "Montserrat", sans-serif; font-weight: 800; font-size: 36px; line-height: 41px; color: var(--teal);
  }
  .stew-photo {
    left: 61px; top: 283px; width: 376px; height: 297px; border-radius: 40% 40% 50% 50%;
    background: radial-gradient(ellipse at 50% 30%, #e9d9a4 0%, #c79a4e 35%, #8a4f25 70%, #5a3016 100%);
  }
  .ingredients-title { left: 459px; top: 166px; font-size: 28px; font-weight: 700; color: var(--ink); }
  .back .checklist { left: 459px; top: 210px; width: 340px; font-size: 27px; line-height: 33px; font-weight: 500; }
  .back .checklist li { margin-bottom: 8px; }
  .method {
    left: 60px; width: 701px; top: 622px; text-align: center; font-size: 27px; line-height: 33px;
  }
  .yield { left: 0; width: 821px; top: 945px; text-align: center; font-size: 29px; font-weight: 700; }

  .elders { left: 0; top: 988px; width: 821px; height: 276px; }
  .elders .tiles-left {
    position: absolute; left: 0; top: 0; width: 274px; height: 276px;
    background: linear-gradient(135deg, #5cb7c9 0%, #e58a4a 45%, #f0c24a 100%);
  }
  .elders .tiles-right {
    position: absolute; left: 719px; top: 0; width: 102px; height: 276px;
    background: linear-gradient(180deg, #e58a4a 0%, #5cb7c9 55%, #f0c24a 100%);
  }
  .elders .elders-text {
    position: absolute; left: 274px; top: 0; width: 445px; height: 276px; background: var(--teal-dark);
    color: #fff; font-weight: 700; font-size: 31px; line-height: 37px; padding: 22px 20px 0 22px;
  }

  .more-title {
    left: 0; width: 821px; top: 1325px; text-align: center;
    font-family: "Roboto", sans-serif; font-weight: 700; font-size: 40px; color: var(--maroon);
  }
  .more-sub {
    left: 0; width: 821px; top: 1374px; text-align: center; font-size: 30px; font-weight: 500; font-style: italic; color: var(--teal);
  }
  .link-pill {
    left: 82px; width: 658px; height: 87px; border-radius: 44px; background: var(--maroon);
    text-align: center; padding-top: 11px;
  }
  .link-pill.first { top: 1424px; }
  .link-pill.second { top: 1536px; }
  .link-name { font-weight: 700; font-size: 30px; color: var(--peach); line-height: 36px; }
  .link-url { font-weight: 300; font-size: 22px; color: var(--peach); line-height: 28px; }

  .org { left: 122px; top: 1655px; width: 620px; height: 150px; display: flex; align-items: center; gap: 26px; }
  .org-dot { width: 140px; height: 140px; border-radius: 50%; background: var(--teal); flex: none; }
  .org-name { font-family: "Montserrat", sans-serif; font-weight: 800; font-size: 36px; line-height: 42px; color: var(--teal); }
</style>
</head>
<body>

<div class="side-label front-label">FRONT</div>

<section class="card front">
  <div class="food-collage" role="img" aria-label="Collage of healthy food: brown rice, salmon with vegetables, fresh salad and berries"></div>
  <h1 class="title-line one">SUNRISE TABLE</h1>
  <div class="title-line two">RIVER WALK</div>
  <h2 class="section-title">OPEN WINDOW</h2>
  <p class="intro">Making small changes in what and how you eat can make you feel better and stay healthier longer. Healthy food choices may be good for your brain, energy, mood and health.</p>
  <div class="zigzag-band" role="img" aria-label="Woven zigzag border pattern"></div>
  <div class="bar changes">LITTLE CHANGES THAT MAKE A BIG DIFFERENCE:</div>
  <ul class="checklist">
    <li>Start today!</li>
    <li>Write down what, when, and how much you eat for three days</li>
    <li>Set SMART goals (Specific, Measurable, Attainable, Relevant &amp; Timebound), like: <strong>“I will eat one piece of fruit at breakfast three times this week.”</strong></li>
    <li>Make just 1 or 2 changes at a time until they become a habit</li>
    <li>Focus more on eating healthy food versus not eating unhealthy food</li>
    <li>Make a game plan for the times you get tempted to eat unhealthy foods</li>
    <li>Involve the whole family in setting goals</li>
    <li>Name your main reason to eat healthier and feel better, like <strong>“More energy to go to church and tribal cultural events.”</strong></li>
  </ul>
  <div class="bar doctor">TALK TO YOUR DOCTOR ABOUT HEALTHIER EATING TO<br>MAKE YOU FEEL BETTER AND STAY HEALTHIER LONGER.</div>
  <blockquote class="quote">
    <p class="quote-text"><span class="quote-mark">“</span> When it comes to traditional foods, for me it’s something more than just food, it’s my heritage. <span class="quote-mark">”</span></p>
    <p class="quote-by">Marisol Tevan (Desert River Nation)</p>
  </blockquote>
  <div class="rule"></div>
  <p class="tagline">MAKING SMALL, PRACTICAL CHANGES CAN HELP YOU<br>ACHIEVE YOUR HEALTH GOALS.</p>
  <p class="funding">This product is supported by the Northfield Health Fund (NHF) of the Meridian Council (MC) as part of a financial assistance award totaling $348,711 with 100 percent funded by NHF/MC. The contents are those of the author(s) and do not necessarily represent the official views of, nor an endorsement, by NHF/MC, or the Council.</p>
  <div class="bottom-strip"></div>
</section>

<div class="side-label back-label">BACK</div>

<section class="card back">
  <h2 class="make-title">MAKE THIS <span>AT HOME</span></h2>
  <h3 class="recipe-name">O’ODHAM<br>WHITE TEPARY<br>BEAN STEW</h3>
  <div class="stew-photo" role="img" aria-label="Wooden bowl of white tepary bean stew with meat"></div>
  <p class="ingredients-title">Ingredients:</p>
  <ul class="checklist">
    <li>1 cup dried tepary beans, rinsed &amp; picked through (substitute Navy Beans or Great Northern beans)</li>
    <li>10 cups of water</li>
    <li>1 tsp. salt</li>
    <li>1 lb. oxtails, beef short ribs, deer, rabbit, or chicken</li>
  </ul>
  <p class="method">Put beans, water, and salt in a stockpot. Bring to a boil, reduce heat and simmer, covered, for one hour and a half. Add meat to the bean mixture, cover and cook for one more hour, or until beans are tender and meat is falling off the bone. If using a crockpot, place water and all other ingredients in the pot, cover, and set to high. Cook for 8 hours or until the meat is falling off the bone and the beans are tender.</p>
  <p class="yield">Makes 8 – 10 cups.</p>
  <div class="elders">
    <div class="tiles-left" role="img" aria-label="Geometric tiles with leaf, fish, sun and corn motifs"></div>
    <p class="elders-text">Elders are our keepers of traditional knowledge about food and ways of life. You play an important role in sharing this knowledge with younger generations.</p>
    <div class="tiles-right" role="img" aria-label="Geometric tiles with plant motifs"></div>
  </div>
  <div class="zigzag-band" role="img" aria-label="Woven zigzag border pattern"></div>
  <h2 class="more-title">FOR MORE INFORMATION</h2>
  <p class="more-sub">About Goal Setting</p>
  <div class="link-pill first">
    <p class="link-name">Society for Everyday Nutrition</p>
    <p class="link-url">https://lnk.example/GoalSettingVideo</p>
  </div>
  <div class="link-pill second">
    <p class="link-name">Harbor Hill Medicine</p>
    <p class="link-url">https://lnk.example/HHSmartGoals</p>
  </div>
  <div class="org">
    <div class="org-dot"></div>
    <p class="org-name">KITE LANE<br>RESOURCE CENTER</p>
  </div>
  <p class="funding">This product is supported by the Northfield Health Fund (NHF) of the Meridian Council (MC) as part of a financial assistance award totaling $348,711 with 100 percent funded by NHF/MC. The contents are those of the author(s) and do not necessarily represent the official views of, nor an endorsement, by NHF/MC, or the Council.</p>
  <div class="bottom-strip"></div>
</section>

</body>
</html>
```